Business Card Design

We are an all natural, organic, salon and spa. I have bought cards on here and have an account. I love the designs that can be simple but at the same time have vines or green leaves, lady profile etc. but not too much. Our name is quite lengthy and it does take up space. I want the slogan: Beauty...inspired by nature! to be on the card somewhere if possible. We also have an Eco friendly boutique and retail organic products.
We need the back side for appointment information. Our lighted box sign has 3 leaves sprouting but was considering changing to have all match even on our website so we can brand our name and logo.
We are classy but down to earth at the same time. If you need to look at our account at old cards or go to our website at www.willowmerepuresalon.example to see some pictures and get a feel of what we look like that would be great.
I am tired of looking around trying to find what is best for us. I need this done pretty soon as I am in need of cards really soon. I can order a box of what we use now if need be. I want whatever we have to be ours to use and not copied.

Target Market(s)

Women of middle age to 60's plus. and health conscious, cancer survivors or presently going through.

Industry/Entity Type

Boutique

Contact Information for Business Card

Willowmere Pure Salon & Spa Slogan branding: Beauty...inspired by nature!
1187 W. Dunmore Crest Bvld. Suite 318
Ocala, Fl. 34470
352-418-7091
www.willowmerepuresalon.example

Colors
acd036
9bcb3c
cadf82

Requirements
Must have
• Fonts that are more organic looking on our sign, but please give me options
Hair or lady's face, profile etc. Has to convey it's a salon and spa by seeing the logo.
Green color fonts for our name. Maybe another color somewhere...lips of color to go with the apple green...etc.
Backside has to have appointment schedule
Nice to have

Should not have
• Clients should not think of this place as an herbal supplement store so we need something that says salon and spa.

```html
<!DOCTYPE html>
<html lang="en">
<head>
<meta charset="utf-8">
<title>Willowmere Pure Salon &amp; Spa — Business Card</title>
<link rel="stylesheet" href="https://fonts.googleapis.com/css2?family=Libre+Baskerville:wght@700&family=Questrial&display=swap">
<style>
  :root {
    --apple-green: #acd036;
    --leaf-green: #9bcb3c;
    --pale-green: #cadf82;
    --bright-green: #c4e23e;
    --deep-green: #5f8f1e;
    --ink-grey: #7a7a7a;
    --line-grey: #9a9a9a;
    --card-white: #ffffff;
    --backdrop: #eceae6;
  }
  * { box-sizing: border-box; margin: 0; padding: 0; }
  html, body { width: 1200px; height: 1000px; overflow: hidden; }
  body {
    background: var(--backdrop);
    font-family: "Questrial", "Helvetica Neue", Arial, sans-serif;
    position: relative;
  }
  .card {
    position: absolute;
    left: 210px;
    width: 780px;
    height: 446px;
    border-radius: 30px;
    overflow: hidden;
    box-shadow: 0 6px 22px rgba(0,0,0,0.14);
  }
  .brand-name {
    font-family: "Libre Baskerville", "Times New Roman", serif;
    font-weight: 700;
    display: flex;
    align-items: center;
    text-transform: uppercase;
    white-space: nowrap;
    letter-spacing: 0.5px;
  }
  .brand-mark { border-radius: 50%; flex: none; }

  /* ---------- Front ---------- */
  .card-front {
    top: 38px;
    background: radial-gradient(ellipse at 50% 38%, var(--bright-green) 0%, var(--leaf-green) 55%, #86bd34 100%);
  }
  .card-front .brand-name {
    position: absolute;
    left: 0; right: 0; top: 170px;
    justify-content: center;
    gap: 14px;
    color: var(--card-white);
    font-size: 28px;
  }
  .card-front .brand-mark { width: 30px; height: 30px; background: var(--card-white); }
  .slogan {
    position: absolute;
    bottom: 70px;
    left: 0; right: 0;
    text-align: center;
    color: var(--card-white);
    font-size: 19px;
    letter-spacing: 1.5px;
    text-transform: uppercase;
  }

  /* ---------- Back ---------- */
  .card-back { top: 516px; background: var(--card-white); }
  .leaf-art {
    position: absolute;
    left: 0; top: 20px;
    width: 300px;
    height: 320px;
    border-radius: 0 140px 140px 0;
    background: linear-gradient(160deg, #8fc23a 0%, var(--apple-green) 50%, var(--pale-green) 100%);
  }
  .back-info {
    position: absolute;
    left: 340px; right: 40px; top: 42px;
  }
  .card-back .brand-name { color: var(--deep-green); font-size: 18px; gap: 10px; }
  .card-back .brand-mark { width: 20px; height: 20px; background: var(--apple-green); }
  .address {
    margin-top: 26px;
    color: var(--ink-grey);
    font-size: 19px;
    line-height: 1.35;
    text-transform: uppercase;
  }
  .phone {
    margin-top: 12px;
    display: flex;
    align-items: center;
    justify-content: flex-end;
    gap: 8px;
    color: var(--ink-grey);
    font-size: 21px;
  }
  .phone svg { width: 22px; height: 22px; }
  .appointment {
    position: absolute;
    left: 340px; right: 36px; top: 262px;
    display: flex;
    align-items: flex-end;
    gap: 8px;
    color: var(--ink-grey);
    font-size: 20px;
    text-transform: uppercase;
  }
  .appointment .fill-line {
    flex: 1;
    border-bottom: 1.5px solid var(--line-grey);
    height: 20px;
  }
  .appointment .ampm { font-size: 13px; }
  .web-band {
    position: absolute;
    left: 0; right: 0; bottom: 0;
    height: 92px;
    background: linear-gradient(90deg, var(--leaf-green), var(--apple-green));
    border-top: 8px solid #d9d9d9;
    display: flex;
    align-items: center;
    justify-content: flex-end;
    padding-right: 44px;
    color: var(--card-white);
    font-size: 26px;
    letter-spacing: 0.5px;
    text-transform: uppercase;
  }
</style>
</head>
<body>
  <section class="card card-front" aria-label="Card front">
    <div class="brand-name"><span class="brand-mark"></span>Willowmere Pure Salon &amp; Spa</div>
    <p class="slogan">Beauty...inspired by nature!</p>
  </section>

  <section class="card card-back" aria-label="Card back, appointment side">
    <div class="leaf-art" role="img" aria-label="Illustration of a green vine with heart-shaped leaves"></div>
    <div class="back-info">
      <div class="brand-name"><span class="brand-mark"></span>Willowmere Pure Salon &amp; Spa</div>
      <p class="address">1187 W. Dunmore Crest Bvld.<br>Suite 318 Ocala, Fl. 34470</p>
      <p class="phone">352-418-7091
        <svg viewBox="0 0 22 22" aria-hidden="true">
          <circle cx="11" cy="11" r="10.5" fill="var(--apple-green)"/>
          <rect x="7.5" y="5" width="7" height="12" rx="1.5" fill="none" stroke="#fff" stroke-width="1.4"/>
          <line x1="10" y1="14.8" x2="12" y2="14.8" stroke="#fff" stroke-width="1.2"/>
        </svg>
      </p>
    </div>
    <div class="appointment">
      <span>Date</span><span class="fill-line"></span>
      <span>Time</span><span class="fill-line"></span>
      <span class="ampm">AM/PM</span>
    </div>
    <div class="web-band">www.willowmerepuresalon.example</div>
  </section>
</body>
</html>
```